Exciting, Bold and Modern Landscaping & Turf care company business card

Hello, I own a lawn and landscaping company in Virginia, USA. We would like to design a bold, dynamic, modern business card that really makes us stand out. I tire of all green business cards with crappy, cartoonish clipart grass on them. It needs to be two sided, on one side i need to highlight our turf care division called "Promised Brighter Meadow" We maintain grass, fertilize it, weed control, etc.. We have a green thumbed gopher as our logo that i will attach. I am looking for something, clean and neat but out of the box in style. Im open to all ideas, and would like different options for them. On the other side, i want to highlight our landscaping division "Quiet Harbor Landscaping" In this division we design and install landscapes. Feel free to visit our website for more info or email me with ANY questions. Our busines cards in the past have highlighted our different services, but i don't want to this time. By the time I hand out a business card we are usually already estimating a project and they know what services we offer. I do want them to look at my card and say "wow thats pretty cool" and for them to think "These guys are something different, not just your standard dirt diggers" The logo doesnt have to be on both sides, but it needs to be on the turf care side. Our phone number and website should also be on at least on side, but need not be on both. The phone number is (555)618-4072 as well as the web address as www.MossbrookYardWorks.example. I like for the web address to have caps like that becasue it makes the long address much easier to read. I would like it in full color, printing costs are not my major concern. I also love rounded corners or interesting die cut designs as well, so feel free to wow me. Whether it be a clean white background with a bold photo to an all black card with a gray logo except for his green thumb with silver foil lettering to anything in between, lets go for it. That bieng said i dont want anything cartoonish, we are still a professional service and i want that to come through. THANKS!
Updates
Project Deadline Extended
Reason: changed project to a committed payment. I would like designers to re-evaluate their interest now and give them extra time to submit designs. Thank you.
we have changed our status to a commited payment to entice more submissions. thank you all for your hard work!
Industry/Entity Type
Professional Service
Look and feel
Each slider illustrates characteristics of the customer's brand and the style your logo design should communicate.

```html
<!DOCTYPE html>
<html lang="en">
<head>
<meta charset="utf-8">
<title>Business Card – Front and Back</title>
<link href="https://fonts.googleapis.com/css2?family=PT+Sans:wght@400;700&family=Arimo:wght@400&display=swap" rel="stylesheet">
<style>
  :root {
    --page: #f2f3f2;
    --lime-light: #c3df8a;
    --lime: #a9d25f;
    --lime-deep: #8cc43f;
    --accent: #8dc63f;
    --charcoal: #4a4640;
    --ring-grey: #8e8f91;
    --white: #ffffff;
  }
  * { box-sizing: border-box; margin: 0; padding: 0; }
  html, body { width: 1200px; height: 1004px; overflow: hidden; }
  body {
    background: var(--page);
    display: flex;
    align-items: center;
    justify-content: center;
    gap: 40px;
  }
  .card {
    position: relative;
    width: 540px;
    height: 312px;
    border-radius: 28px;
    overflow: hidden;
    background: var(--charcoal);
  }
  .card__top {
    position: absolute;
    inset: 0 0 auto 0;
    height: 196px;
    background: linear-gradient(160deg, var(--lime-light) 0%, var(--lime) 55%, var(--lime-deep) 100%);
  }
  .title-bar {
    position: absolute;
    top: 72px;
    height: 43px;
    background: var(--charcoal);
    color: var(--white);
    font-family: "PT Sans", sans-serif;
    font-size: 28px;
    line-height: 43px;
    white-space: nowrap;
  }
  .title-bar em { font-style: normal; color: var(--accent); }
  .card--front .title-bar { left: 169px; right: 0; padding-left: 10px; border-radius: 6px 0 0 6px; }
  .card--back .title-bar { left: 0; width: 409px; padding-left: 20px; border-radius: 0 6px 6px 0; }
  .mascot-mark {
    position: absolute;
    left: 50px;
    top: 60px;
    width: 120px;
    height: 120px;
  }
  .front-contact {
    position: absolute;
    top: 212px;
    left: 0;
    right: 0;
    text-align: center;
    color: var(--white);
    font-family: Arimo, sans-serif;
  }
  .front-contact .website { font-size: 25px; }
  .front-contact .phone {
    margin-top: 10px;
    font-size: 17px;
    display: inline-flex;
    align-items: center;
    gap: 10px;
  }
  .ring { position: absolute; }
  .ring--top { left: 459px; top: 57px; }
  .ring--bottom { left: -57px; top: 172px; }
  .address {
    position: absolute;
    top: 222px;
    left: 160px;
    color: var(--white);
    font-family: Arimo, sans-serif;
    font-size: 16px;
    line-height: 20px;
    text-align: center;
  }
  .address .company { display: flex; align-items: center; justify-content: center; gap: 10px; }
</style>
</head>
<body>

<section class="card card--front" aria-label="Turf care side">
  <div class="card__top"></div>
  <svg class="mascot-mark" role="img" aria-label="Turf care mascot logo" viewBox="0 0 120 120">
    <circle cx="60" cy="60" r="54" fill="#4a4640"/>
  </svg>
  <div class="title-bar">Promised <em>Brighter</em> Meadow</div>
  <div class="front-contact">
    <p class="website">www.MossbrookYardWorks.example</p>
    <p class="phone">
      <svg width="18" height="18" viewBox="0 0 24 24" aria-hidden="true">
        <path fill="#8dc63f" d="M6.6 10.8a15.1 15.1 0 0 0 6.6 6.6l2.2-2.2a1 1 0 0 1 1-.25 11.4 11.4 0 0 0 3.6.57 1 1 0 0 1 1 1V20a1 1 0 0 1-1 1A17 17 0 0 1 3 4a1 1 0 0 1 1-1h3.5a1 1 0 0 1 1 1c0 1.25.2 2.45.57 3.57a1 1 0 0 1-.25 1z"/>
      </svg>
      555-618-4072
    </p>
  </div>
</section>

<section class="card card--back" aria-label="Landscaping side">
  <div class="card__top"></div>
  <svg class="ring ring--top" width="120" height="120" viewBox="0 0 120 120" aria-hidden="true">
    <circle cx="60" cy="60" r="46" fill="#a9d25f" stroke="#8e8f91" stroke-width="20"/>
  </svg>
  <svg class="ring ring--bottom" width="120" height="120" viewBox="0 0 120 120" aria-hidden="true">
    <circle cx="60" cy="60" r="46" fill="#a9d25f" stroke="#8e8f91" stroke-width="20"/>
  </svg>
  <div class="title-bar">Quiet <em>Harbor</em> Landscaping</div>
  <div class="address">
    <p class="company">
      <svg width="20" height="18" viewBox="0 0 20 18" aria-hidden="true">
        <path fill="#8dc63f" d="M10 0 0 9h3v9h5v-6h4v6h5V9h3z"/>
      </svg>
      Quiet Harbor Landscaping
    </p>
    <p>4180-27 Alder Ct. Suite 112</p>
    <p>Harbor Town, VA 20000</p>
  </div>
</section>

</body>
</html>
```